BRIGHTDESK - Remote Tech Support Site

We are looking for a new very responsive and simple website for our brand Brightdesk.com - a remote technical support company.

This company supports customers Globally in different countries throughout Eur/ North America / South America / Asia etc (please keep this in mind and integrate into the idea).

Its important to us that the design is very explanatory, the customer should easily be able to figure out that we provide computer support right away ... I like one page responsive type designs as well without a bunch of menu items

Here are some similar sites we like - but still looking for a unique design that fits out brand "brightdesk" - I have upload also some layouts i like (but the designs are not important just the layouts), youll see it includes consumer business etc which is important.

VOLM.COM - I love how clean it is - nice and white easy to see everything

PLUMWIRE247.COM - also nice the layout and responsive one page design makes it easy to use

corvalfix.com - similar to plumwire design as well - you can get the idea im looking for between the two

You will notice those examples are much different then the attachments I added - again this is more of an idea for possible layouts .. attached is also the logo - could inspire color scheme / blue white black etc

Target Market(s)

Home consumers without computer knowledge , older age 45-65, small medium business ... computer repair - slow computers

Industry/Entity Type

Computer Repair

Logo Text

Brightdesk

Coding

Coded - Design and coding required

Number of Pages Required

1 page

Font styles to use
Sans Serif
Other font styles liked:
• your choice responsive

Colors

Designer to choose colors to be used in the design.

Requirements
Must have
• Clean - responsive - professional design - the name says it all - brightdesk
• CALL TO ACTIONS FOR "Get Help Now!" / "Learn More" etc
Nice to have
• We are looking for a new very responsive and simple website for our brand Brightdesk.com - a remote technical support company.
• This company supports customers Globally in different countries throughout Eur/ North America / South America / Asia etc (please keep this in mind and integrate into the idea).
• Its important to us that the design is very explanatory, the customer should easily be able to figure out that we provide computer support right away ... I like one page responsive type designs as well without a bunch of menu items
• Here are some similar sites we like - but still looking for a unique design that fits out brand "brightdesk" - I have upload also some layouts i like (but the designs are not important just the layouts), youll see it includes consumer business etc which is important.
• VOLM.COM - I love how clean it is - nice and white easy to see everything
• PLUMWIRE247.COM - also nice the layout and responsive one page design makes it easy to use
• corvalfix.com - similar to plumwire design as well - you can get the idea im looking for between the two
Should not have
• dark, packed page - bad small font -

```html
<!DOCTYPE html>
<html lang="en">
<head>
<meta charset="utf-8">
<title>Brightdesk – Remote Technical Support</title>
<link href="https://fonts.googleapis.com/css2?family=Open+Sans:wght@400;600;700&family=Ubuntu:wght@400;500;700&display=swap" rel="stylesheet">
<style>
:root{
  --blue:#2a7de1;
  --blue-dark:#1f6cc9;
  --ink:#222629;
  --text:#555b61;
  --muted:#8a9096;
  --line:#e3e6e9;
  --soft:#f2f3f4;
  --white:#ffffff;
  --footer:#1f2327;
  --footer-text:#b7bcc1;
  --card-head:#3a3d41;
}
*{box-sizing:border-box;margin:0;padding:0}
html,body{width:1200px;height:3030px;overflow:hidden}
body{font-family:"Open Sans",Arial,sans-serif;color:var(--text);background:var(--white);position:relative}
h1,h2,h3,h4{font-family:"Ubuntu","Open Sans",sans-serif;font-weight:500;color:var(--ink)}
.accent{color:var(--blue);font-weight:400}
.btn{display:inline-block;border-radius:20px;font-weight:700;font-size:13px;text-decoration:none;text-align:center}
.btn-blue{background:var(--blue);color:var(--white)}
.btn-dark{background:#111;color:var(--white)}
.btn-ghost{border:1.5px solid #6c7177;color:var(--ink);background:var(--white)}

/* header */
.site-header{position:absolute;top:0;left:0;width:1200px;height:93px;border-bottom:3px solid var(--blue);background:var(--white)}
.brand{position:absolute;left:130px;top:22px;display:flex;align-items:center;gap:10px}
.brand-dot{width:46px;height:46px;border-radius:50%;background:var(--blue)}
.brand-name{font-family:"Open Sans",sans-serif;font-size:32px;font-weight:600;color:var(--ink);letter-spacing:-.5px}
.main-nav{position:absolute;left:482px;top:0;display:flex;height:90px}
.main-nav a{display:flex;align-items:center;padding:0 14px;font-size:11px;font-weight:600;color:#333;text-decoration:none;position:relative;white-space:nowrap}
.main-nav a.active{color:var(--blue)}
.main-nav a.active::before{content:"";position:absolute;left:0;right:0;top:0;height:3px;background:var(--blue)}
.nav-phone{position:absolute;left:914px;top:27px;display:flex;align-items:center;gap:14px;font-size:16px;font-weight:600;color:var(--blue);white-space:nowrap}
.nav-phone .ring{width:34px;height:34px;border:2px solid var(--blue);border-radius:50%;display:flex;align-items:center;justify-content:center}

/* hero */
.hero{position:absolute;top:93px;left:0;width:1200px;height:512px;background:linear-gradient(90deg,#c9c7c4 0%,#e6e4e1 35%,#dcdcda 60%,#bfc3c6 100%)}
.hero-copy{position:absolute;left:132px;top:154px}
.hero-title{display:inline-block;background:rgba(255,255,255,.82);padding:6px 22px 8px 20px;font-family:"Open Sans",sans-serif;font-size:38px;font-weight:700;color:#1d1f21}
.hero-title .accent{font-weight:400}
.hero-text{margin-top:12px;width:380px;background:rgba(80,80,80,.55);color:var(--white);font-size:13.5px;line-height:26px;padding:10px 20px}
.hero-actions{margin-top:30px;display:flex;gap:6px}
.hero-actions .btn{width:122px;height:38px;line-height:38px;font-size:12.5px}
.hero-actions .btn-dark{width:106px}
.hero-dots{position:absolute;left:130px;top:430px;display:flex;gap:14px}
.hero-dots span{width:10px;height:10px;border-radius:50%;background:#777}
.hero-dots span.on{background:var(--blue)}

/* section headings */
.section-title{text-align:center;font-size:27px}
.title-rule{display:flex;justify-content:center;gap:4px;margin:8px auto 0}
.title-rule i{display:block;height:2px;width:24px;background:var(--blue)}
.title-rule i+i{width:24px;background:var(--ink)}

/* services */
.services{position:absolute;top:605px;left:0;width:1200px;height:505px;background:var(--soft)}
.services .section-title{margin-top:52px}
.services .lead{text-align:center;font-size:13px;color:var(--text);margin-top:12px}
.service-grid{position:absolute;top:143px;left:132px;display:flex;gap:20px}
.service-card{width:219px;height:290px;background:var(--white);border-top:5px solid var(--blue);box-shadow:0 1px 4px rgba(0,0,0,.12);text-align:center;position:relative}
.cart-tab{position:absolute;right:0;top:0;width:46px;height:40px;background:#f0f1f2;border-bottom-left-radius:40px;display:flex;align-items:center;justify-content:center}
.service-icon{margin:26px auto 0;width:90px;height:90px;border:2.5px solid var(--blue);border-radius:50%;display:flex;align-items:center;justify-content:center}
.service-card h3{font-family:"Open Sans",sans-serif;font-size:12.5px;font-weight:600;color:#333;margin-top:18px}
.service-card p{font-size:11px;line-height:18px;color:var(--muted);width:150px;margin:8px auto 0}
.service-card .btn{margin-top:14px;width:86px;height:32px;line-height:29px;font-size:11px;font-weight:600}

/* features */
.features{position:absolute;top:1110px;left:0;width:1200px;height:420px;background:var(--white)}
.features-photo{position:absolute;left:0;top:0;width:660px;height:420px;background:linear-gradient(90deg,#8b98a6 0%,#c7ced5 45%,#eef0f2 80%,#ffffff 100%)}
.features-copy{position:absolute;left:716px;top:56px}
.features-copy h2{font-family:"Open Sans",sans-serif;font-size:26px;font-weight:700;line-height:40px}
.check-list{list-style:none;margin-top:24px}
.check-list li{display:flex;align-items:center;gap:14px;font-size:13px;color:var(--text);height:40px}
.features-copy .btn{margin-top:22px;width:146px;height:38px;line-height:38px;font-size:12px}

/* how it works */
.how{position:absolute;top:1530px;left:0;width:1200px;height:363px}
.how .section-title{margin-top:58px;font-family:"Open Sans",sans-serif;font-weight:700}
.steps{position:absolute;top:138px;left:120px;width:960px;display:flex;justify-content:space-between}
.step{width:260px;text-align:center}
.step-icon{height:96px;display:flex;align-items:flex-end;justify-content:center}
.step h4{font-family:"Open Sans",sans-serif;font-size:13px;font-weight:600;color:#333;margin-top:14px}
.step p{font-size:11px;line-height:20px;color:var(--text);margin-top:6px}
.step-arrow{position:absolute;top:30px}

/* pricing */
.pricing{position:absolute;top:1893px;left:0;width:1200px;height:520px;background:var(--blue)}
.pricing .section-title{color:var(--white);margin-top:48px;font-family:"Open Sans",sans-serif;font-weight:700}
.pricing .section-title .light{font-weight:400}
.price-grid{position:absolute;top:125px;left:132px;display:flex;gap:33px}
.price-card{width:290px;height:320px;background:var(--white);box-shadow:0 4px 10px rgba(0,0,0,.25);text-align:center}
.price-head{height:58px;background:var(--card-head);color:var(--white);font-family:"Open Sans",sans-serif;font-weight:700;font-size:15px;padding-top:18px;position:relative}
.price-head::after{content:"";position:absolute;left:0;bottom:-22px;border-left:145px solid transparent;border-right:145px solid transparent;border-top:22px solid var(--card-head)}
.price{margin-top:36px;color:var(--blue);font-family:"Open Sans",sans-serif;font-size:32px;font-weight:600}
.price small{font-size:11px;font-weight:700;font-style:italic}
.setup{font-size:12px;color:#333;margin-top:6px}
.price-rule{width:240px;height:1px;background:var(--line);margin:16px auto 10px}
.price-card li{list-style:none;font-size:11px;color:var(--muted);line-height:30px}
.price-card .btn{margin-top:6px;width:96px;height:32px;line-height:32px;font-size:11px}

/* best */
.best{position:absolute;top:2413px;left:0;width:1200px;height:377px}
.best-copy{position:absolute;left:132px;top:48px;width:500px}
.best-copy h2{font-family:"Open Sans",sans-serif;font-size:26px;font-weight:700;line-height:38px}
.best-copy h2 .accent{font-weight:400}
.best-copy p{font-size:11px;line-height:20px;color:var(--text);margin-top:22px}
.best-copy p+p{margin-top:16px}
.perk-list{position:absolute;left:668px;top:60px;list-style:none}
.perk{display:flex;gap:16px;height:72px}
.perk-icon{width:44px;display:flex;justify-content:center;padding-top:2px}
.perk h4{font-family:"Open Sans",sans-serif;font-size:13px;font-weight:600;color:#222}
.perk p{font-size:10.5px;color:var(--text);margin-top:5px}

/* footer */
.site-footer{position:absolute;top:2790px;left:0;width:1200px;height:240px;background:var(--footer);color:var(--footer-text)}
.footer-brand{position:absolute;left:132px;top:34px}
.footer-brand .brand-line{display:flex;align-items:center;gap:8px}
.footer-brand .brand-dot{width:34px;height:34px;background:var(--white)}
.footer-brand .brand-name{color:var(--white);font-size:26px}
.footer-brand p{font-size:10.5px;line-height:19px;width:240px;margin-top:14px}
.footer-col h5{font-family:"Open Sans",sans-serif;font-size:13px;font-weight:700;color:var(--white);letter-spacing:.3px}
.plans-col{position:absolute;left:425px;top:34px}
.plans-col li{list-style:none;font-size:10.5px;line-height:24px;margin-top:2px}
.plans-col ul{margin-top:10px}
.news-col{position:absolute;left:578px;top:34px}
.news-col p{font-size:10.5px;margin-top:14px}
.news-form{margin-top:14px;display:flex;width:270px;height:40px}
.news-form span{flex:1;background:var(--white);border-radius:20px 0 0 20px;font-size:10px;color:#999;padding:13px 0 0 20px}
.news-form b{width:84px;background:var(--blue);border-radius:0 20px 20px 0;color:var(--white);font-size:12px;text-align:center;line-height:40px}
.trust-col{position:absolute;left:912px;top:34px}
.badges{margin-top:14px;position:relative;width:170px;height:110px}
.badge-a{position:absolute;left:0;top:0;width:76px;height:30px;background:#eef0f1;border-radius:3px}
.badge-b{position:absolute;left:80px;top:0;width:56px;height:52px;background:#c8262e;border-radius:50%}
.badge-c{position:absolute;left:4px;top:42px;width:66px;height:66px;background:#c9a227;border-radius:50%}
.footer-bottom{position:absolute;left:132px;right:132px;top:188px;border-top:1px solid #33383d;padding-top:18px;display:flex;justify-content:space-between;font-size:10px}
.social{display:flex;align-items:center;gap:8px}
.social i{display:block;width:26px;height:26px;border-radius:50%;background:var(--blue)}
</style>
</head>
<body>

<header class="site-header">
  <div class="brand"><span class="brand-dot"></span><span class="brand-name">brightdesk</span></div>
  <nav class="main-nav">
    <a class="active" href="#">HOME</a>
    <a href="#">ABOUT US</a>
    <a href="#">SERVICES</a>
    <a href="#">CONTACT US</a>
    <a href="#">FAQS</a>
  </nav>
  <div class="nav-phone">
    <span class="ring"><svg width="16" height="16" viewBox="0 0 24 24"><path d="M6.6 10.8a15 15 0 0 0 6.6 6.6l2.2-2.2c.3-.3.7-.4 1-.2 1.1.4 2.3.6 3.6.6.6 0 1 .4 1 1V20c0 .6-.4 1-1 1A17 17 0 0 1 3 4c0-.6.4-1 1-1h3.5c.6 0 1 .4 1 1 0 1.3.2 2.5.6 3.6.1.3 0 .7-.2 1z" fill="#2a7de1"/></svg></span>
    (555) 013-2480
  </div>
</header>

<section class="hero">
  <div role="img" aria-label="Photo of a technician in glasses working at a laptop in a bright office" style="position:absolute;inset:0"></div>
  <div class="hero-copy">
    <h1 class="hero-title">Technical <span class="accent">Support</span></h1>
    <p class="hero-text">Eiusmod tempor incididunt ut labore et quaenim ad minim veniam, quis nostrud exercit...</p>
    <div class="hero-actions">
      <a class="btn btn-blue" href="#">Get Help Now!</a>
      <a class="btn btn-dark" href="#">Learn More</a>
    </div>
  </div>
  <div class="hero-dots"><span class="on"></span><span></span><span></span></div>
</section>

<section class="services">
  <h2 class="section-title">Our <span class="accent">Services</span></h2>
  <div class="title-rule"><i></i><i></i></div>
  <p class="lead">Brightdesk provides the following plans:</p>
  <div class="service-grid">
    <article class="service-card">
      <span class="cart-tab"><svg width="18" height="16" viewBox="0 0 24 22"><path d="M1 2h4l3 12h12l3-9H7" fill="none" stroke="#222" stroke-width="2.2"/><circle cx="9" cy="19" r="2" fill="#222"/><circle cx="19" cy="19" r="2" fill="#222"/></svg></span>
      <div class="service-icon"><svg width="50" height="50" viewBox="0 0 50 50"><path d="M12 32a9 9 0 0 1 2-17 12 12 0 0 1 23 2 8 8 0 0 1 1 15z" fill="none" stroke="#2a7de1" stroke-width="2.5"/><path d="M25 22l9 3v7c0 6-4 9-9 11-5-2-9-5-9-11v-7z" fill="#2a7de1"/></svg></div>
      <h3>Complete Privacy Protection</h3>
      <p>Lorem ipsum dolor ascing mod tempor incididuntlabore magna aliqua...</p>
      <a class="btn btn-ghost" href="#">Learn More</a>
    </article>
    <article class="service-card">
      <span class="cart-tab"><svg width="18" height="16" viewBox="0 0 24 22"><path d="M1 2h4l3 12h12l3-9H7" fill="none" stroke="#222" stroke-width="2.2"/><circle cx="9" cy="19" r="2" fill="#222"/><circle cx="19" cy="19" r="2" fill="#222"/></svg></span>
      <div class="service-icon"><svg width="50" height="50" viewBox="0 0 50 50"><rect x="6" y="10" width="34" height="24" rx="2" fill="none" stroke="#2a7de1" stroke-width="2.5"/><path d="M18 40h12M24 34v6" stroke="#2a7de1" stroke-width="2.5"/><path d="M37 26l7 2v6c0 4-3 6-7 8-4-2-7-4-7-8v-6z" fill="#2a7de1"/></svg></div>
      <h3>Online Identity Theft Protection</h3>
      <p>Lorem ipsum dolor ascing mod tempor incididuntlabore magna aliqua...</p>
      <a class="btn btn-ghost" href="#">Learn More</a>
    </article>
    <article class="service-card">
      <span class="cart-tab"><svg width="18" height="16" viewBox="0 0 24 22"><path d="M1 2h4l3 12h12l3-9H7" fill="none" stroke="#222" stroke-width="2.2"/><circle cx="9" cy="19" r="2" fill="#222"/><circle cx="19" cy="19" r="2" fill="#222"/></svg></span>
      <div class="service-icon"><svg width="50" height="50" viewBox="0 0 50 50"><path d="M6 18l18-6 18 6-18 6z" fill="#2a7de1"/><path d="M6 25l18 6 18-6M6 32l18 6 18-6" fill="none" stroke="#2a7de1" stroke-width="3"/><path d="M36 12l7 2v6c0 4-3 6-7 8-4-2-7-4-7-8v-6z" fill="#1f6cc9" stroke="#fff" stroke-width="1.5"/></svg></div>
      <h3>Real-Time System Reporting</h3>
      <p>Lorem ipsum dolor ascing mod tempor incididuntlabore magna aliqua...</p>
      <a class="btn btn-ghost" href="#">Learn More</a>
    </article>
    <article class="service-card">
      <span class="cart-tab"><svg width="18" height="16" viewBox="0 0 24 22"><path d="M1 2h4l3 12h12l3-9H7" fill="none" stroke="#222" stroke-width="2.2"/><circle cx="9" cy="19" r="2" fill="#222"/><circle cx="19" cy="19" r="2" fill="#222"/></svg></span>
      <div class="service-icon"><svg width="50" height="50" viewBox="0 0 50 50"><ellipse cx="22" cy="11" rx="14" ry="5" fill="#2a7de1"/><path d="M8 15v8c0 3 6 5 14 5s14-2 14-5v-8c0 3-6 5-14 5S8 18 8 15zM8 27v8c0 3 6 5 14 5s14-2 14-5v-8c0 3-6 5-14 5S8 30 8 27z" fill="#2a7de1"/><rect x="32" y="32" width="12" height="10" rx="1.5" fill="#1f6cc9" stroke="#fff" stroke-width="1.5"/><path d="M35 32v-3a3 3 0 0 1 6 0v3" fill="none" stroke="#1f6cc9" stroke-width="2"/></svg></div>
      <h3>Safe and Secure Connection</h3>
      <p>Lorem ipsum dolor ascing mod tempor incididuntlabore magna aliqua...</p>
      <a class="btn btn-ghost" href="#">Learn More</a>
    </article>
  </div>
</section>

<section class="features">
  <div class="features-photo" role="img" aria-label="Photo of a smiling support agent typing on a laptop in an office"></div>
  <div class="features-copy">
    <h2>Real-Time Support <span class="accent">Features<br>and Benefits</span></h2>
    <ul class="check-list">
      <li><svg width="16" height="16" viewBox="0 0 16 16"><circle cx="8" cy="8" r="7" fill="none" stroke="#2a7de1" stroke-width="1.6"/><path d="M5 8h6M8.5 5.5 11 8l-2.5 2.5" fill="none" stroke="#2a7de1" stroke-width="1.6"/></svg>24/7 Real-Time Technician Support</li>
      <li><svg width="16" height="16" viewBox="0 0 16 16"><circle cx="8" cy="8" r="7" fill="none" stroke="#2a7de1" stroke-width="1.6"/><path d="M5 8h6M8.5 5.5 11 8l-2.5 2.5" fill="none" stroke="#2a7de1" stroke-width="1.6"/></svg>The best Security Software in the market</li>
      <li><svg width="16" height="16" viewBox="0 0 16 16"><circle cx="8" cy="8" r="7" fill="none" stroke="#2a7de1" stroke-width="1.6"/><path d="M5 8h6M8.5 5.5 11 8l-2.5 2.5" fill="none" stroke="#2a7de1" stroke-width="1.6"/></svg>Regular tune-ups and optimization</li>
      <li><svg width="16" height="16" viewBox="0 0 16 16"><circle cx="8" cy="8" r="7" fill="none" stroke="#2a7de1" stroke-width="1.6"/><path d="M5 8h6M8.5 5.5 11 8l-2.5 2.5" fill="none" stroke="#2a7de1" stroke-width="1.6"/></svg>Setup and installation included</li>
    </ul>
    <a class="btn btn-blue" href="#">Become a Member</a>
  </div>
</section>

<section class="how">
  <h2 class="section-title">How it <span class="accent">Works?</span></h2>
  <div class="steps">
    <div class="step">
      <div class="step-icon"><svg width="90" height="90" viewBox="0 0 90 90"><rect x="20" y="4" width="50" height="16" rx="2" fill="#9a9ea2"/><rect x="20" y="24" width="50" height="16" rx="2" fill="#9a9ea2"/><rect x="20" y="44" width="50" height="16" rx="2" fill="#9a9ea2"/><circle cx="28" cy="12" r="2.5" fill="#fff"/><circle cx="28" cy="32" r="2.5" fill="#fff"/><circle cx="28" cy="52" r="2.5" fill="#fff"/><path d="M45 60v18M16 80h58" stroke="#9a9ea2" stroke-width="3"/><circle cx="45" cy="80" r="5" fill="#fff" stroke="#9a9ea2" stroke-width="3"/></svg></div>
      <h4>FREE Diagnostic</h4>
      <p>Get a diagnostic, FOR FREE! Get a free consultation with our staff.</p>
    </div>
    <div class="step">
      <div class="step-icon"><svg width="90" height="90" viewBox="0 0 90 90"><path d="M45 4l34 10v26c0 22-16 36-34 44-18-8-34-22-34-44V14z" fill="#9a9ea2"/><circle cx="62" cy="66" r="14" fill="#fff"/><path d="M55 66l5 5 9-10" fill="none" stroke="#9a9ea2" stroke-width="3.5"/></svg></div>
      <h4>Get Fixed</h4>
      <p>Get fixed, IMMEDIATELY! Our staff will solve your computer issues right before your eyes.</p>
    </div>
    <div class="step">
      <div class="step-icon"><svg width="100" height="90" viewBox="0 0 100 90"><path d="M24 64a16 16 0 0 1-2-32 24 24 0 0 1 46-4 18 18 0 0 1 8 36z" fill="#9a9ea2"/><path d="M50 80V40M37 52l13-13 13 13" fill="none" stroke="#fff" stroke-width="5"/><path d="M50 64v22" stroke="#9a9ea2" stroke-width="5"/></svg></div>
      <h4>Backup your information!</h4>
      <p>Saving your files is now EASY! You will be able to retain your personal files without any loss of data.</p>
    </div>
  </div>
  <svg class="step-arrow" style="left:382px;top:158px" width="100" height="40" viewBox="0 0 100 40"><path d="M4 34C30 6 66 4 90 22" fill="none" stroke="#e3e4e5" stroke-width="6"/><path d="M80 12l14 12-18 4z" fill="#e3e4e5"/></svg>
  <svg class="step-arrow" style="left:708px;top:158px" width="100" height="40" viewBox="0 0 100 40"><path d="M4 34C30 6 66 4 90 22" fill="none" stroke="#e3e4e5" stroke-width="6"/><path d="M80 12l14 12-18 4z" fill="#e3e4e5"/></svg>
</section>

<section class="pricing">
  <h2 class="section-title">Membership Pricing <span class="light">&amp; Plans</span></h2>
  <div class="price-grid">
    <article class="price-card">
      <div class="price-head">PREMIUM</div>
      <div class="price">$19.99 <small>/ Monthly</small></div>
      <div class="setup">($249-$300 setup fee)</div>
      <div class="price-rule"></div>
      <ul><li>Regular 90-Day Optimization</li><li>Unlimited 24/7 Tier 3</li><li>Technician Support</li></ul>
      <a class="btn btn-blue" href="#">Learn More</a>
    </article>
    <article class="price-card">
      <div class="price-head">PREMIUM PLUS</div>
      <div class="price">$29.99 <small>/ Monthly</small></div>
      <div class="setup">($249-$300 setup fee)</div>
      <div class="price-rule"></div>
      <ul><li>Regular 90-Day Optimization</li><li>Unlimited 24/7 Tier 3</li><li>Technician Support</li></ul>
      <a class="btn btn-blue" href="#">Learn More</a>
    </article>
    <article class="price-card">
      <div class="price-head">PLATINUM</div>
      <div class="price">$39.99 <small>/ Monthly</small></div>
      <div class="setup">($249-$300 setup fee)</div>
      <div class="price-rule"></div>
      <ul><li>Regular 90-Day Optimization</li><li>Unlimited 24/7 Tier 3</li><li>Technician Support</li></ul>
      <a class="btn btn-blue" href="#">Learn More</a>
    </article>
  </div>
</section>

<section class="best">
  <div class="best-copy">
    <h2>All the Best Features<br><span class="accent">At the Best Price!</span></h2>
    <p>Lorem ipsum dolor sit amet, consectetur adipiscing elit, sed do eiusmod tempor incididunt ut labore et dolore magna aliqua. Ut enim ad minim veniam, quis nostrud exercitation ullamco laboris nisi ut aliquip ex ea commodo consequat.</p>
    <p>Duis aute irure dolor in reprehenderit in voluptate velit esse cillum dolore eu fugiat nulla pariatur. Excepteur sint occaecat cupidatat non proident, sunt in culpa qui officia deserunt mollit anim id est laborum Nemo enim ipsam...</p>
  </div>
  <ul class="perk-list">
    <li class="perk"><span class="perk-icon"><svg width="40" height="40" viewBox="0 0 40 40"><circle cx="20" cy="20" r="16" fill="none" stroke="#222" stroke-width="4"/><path d="M9 31L31 9" stroke="#222" stroke-width="4"/></svg></span><div><h4>Ad Blocker</h4><p>Avoid unwanted Pop-ups with the newest Ad Blocking technology.</p></div></li>
    <li class="perk"><span class="perk-icon"><svg width="44" height="36" viewBox="0 0 44 36"><rect x="7" y="4" width="30" height="20" rx="1.5" fill="none" stroke="#222" stroke-width="3"/><path d="M2 29h40" stroke="#222" stroke-width="4"/></svg></span><div><h4>Regular Tune-Ups</h4><p>Get a Regular Tune-Up and Optimization every 90 days.</p></div></li>
    <li class="perk"><span class="perk-icon"><svg width="40" height="40" viewBox="0 0 40 40"><path d="M18 4a16 16 0 1 0 16 18H18z" fill="#222"/><path d="M22 2v16h16A16 16 0 0 0 22 2z" fill="#222"/></svg></span><div><h4>System Reports</h4><p>Get support for up to 4 multiple devices. Ask about our Family Plans.</p></div></li>
    <li class="perk"><span class="perk-icon"><svg width="40" height="40" viewBox="0 0 40 40"><rect x="3" y="4" width="34" height="24" rx="2" fill="#222"/><path d="M16 28v6M24 28v6M11 36h18" stroke="#222" stroke-width="3"/></svg></span><div><h4>Multiple Devices</h4><p>Get support for up to 4 multiple devices. Ask about our Family Plans.</p></div></li>
  </ul>
</section>

<footer class="site-footer">
  <div class="footer-brand">
    <div class="brand-line"><span class="brand-dot"></span><span class="brand-name">brightdesk</span></div>
    <p>We are a group of technicians who work round the clock to ensure that your PC works perfectly. Get your computer free of suspicious software and have a healthy system.</p>
  </div>
  <div class="footer-col plans-col">
    <h5>PLANS</h5>
    <ul><li>Premium Plan</li><li>Premium Plus Plan</li><li>Platinum Plan</li></ul>
  </div>
  <div class="footer-col news-col">
    <h5>NEWSLETTER SIGNUP</h5>
    <p>Sign up for our regular informational newsletters</p>
    <div class="news-form"><span>Enter Your Email Address</span><b>Sign Up</b></div>
  </div>
  <div class="footer-col trust-col">
    <h5>TRUSTED BY</h5>
    <div class="badges"><span class="badge-a"></span><span class="badge-b"></span><span class="badge-c"></span></div>
  </div>
  <div class="footer-bottom">
    <span>Copyrights © brightdesk . 2017 | Allrights Reserved.</span>
    <span class="social">Connect With Us : <i></i><i></i></span>
  </div>
</footer>

</body>
</html>
```